Yacht Charter Broker needs a magazine page design

We are a travel agent for yachts called Velmoria Yacht Charters. www.velmoriacharters.example We are advertising in a magazine at the grand pacer equine fair - https://plgequinefair.example/ - and need a high-end luxury feeling magazine page.

Target Market(s)

Vacation goers looking to charter a crewed yacht.

Industry/Entity Type

Travel Agent

Requirements
Must have
• luxury feel. logo. website and social media icons if you feel necessary. Our motto is: Inhale. Exhale. Sail.
• Catamaran picture, snorkeling and other island, water looking pictures.
Nice to have
• Open to your design.
Should not have
• Nothing comes to mind.

```html
<!DOCTYPE html>
<html lang="en">
<head>
<meta charset="utf-8">
<title>Velmoria Yacht Charters – Magazine Page</title>
<link href="https://fonts.googleapis.com/css2?family=Cinzel:wght@400&family=Montserrat:wght@400;500;700&display=swap" rel="stylesheet">
<style>
  :root {
    --navy: #0c2a5f;
    --navy-soft: #163a78;
    --white: #ffffff;
    --line: rgba(255,255,255,0.55);
    --footer-dark: #3b3b3b;
    --backdrop: #e9e9ea;
  }
  * { box-sizing: border-box; margin: 0; padding: 0; }
  html, body {
    width: 1000px; height: 1200px; overflow: hidden;
    background: var(--backdrop);
  }
  .page {
    position: absolute; left: 90px; top: 68px;
    width: 820px; height: 1064px;
    background: var(--navy);
    font-family: "Montserrat", sans-serif;
    color: var(--white);
  }
  .brand {
    position: absolute; left: 0; top: 50px; width: 100%;
    text-align: center;
  }
  .brand-name {
    font-family: "Cinzel", serif; font-weight: 400;
    font-size: 48px; letter-spacing: 5px; line-height: 1;
  }
  .brand-tagline {
    font-family: "Cinzel", serif; font-size: 12.5px;
    letter-spacing: 2.5px; margin-top: 8px; padding-left: 150px;
  }
  .photo { position: absolute; }
  .photo-deck {
    left: 0; top: 178px; width: 592px; height: 494px;
    background: linear-gradient(180deg, #c8b590 0%, #7c8a86 22%, #34505c 45%, #1b2c36 75%, #10202a 100%);
  }
  .photo-guests {
    left: 0; top: 604px; width: 272px; height: 181px;
    background: linear-gradient(180deg, #e6d1a2 0%, #a98d66 40%, #4a4036 75%, #2a2a2a 100%);
  }
  .photo-aerial {
    left: 414px; top: 546px; width: 406px; height: 239px;
    background: radial-gradient(ellipse at 65% 55%, #5fd0e3 0%, #1aa3c8 45%, #0b6e9a 100%);
  }
  .motto-panel {
    position: absolute; left: 463px; top: 228px; width: 357px; height: 316px;
    background: var(--navy);
  }
  .motto-frame {
    position: absolute; left: 14px; top: 13px; width: 270px; height: 210px;
    border: 1px solid var(--line);
    display: flex; flex-direction: column; align-items: center; justify-content: center;
    text-align: center; line-height: 1;
  }
  .motto-line { font-size: 45px; font-weight: 400; letter-spacing: 0.5px; margin-bottom: 4px; }
  .motto-strong { font-size: 72px; font-weight: 700; letter-spacing: 1px; margin-top: 4px; }
  .leaders {
    position: absolute; left: 0; top: 830px; width: 100%;
    text-align: center; font-size: 24px; font-weight: 500; letter-spacing: 0.5px;
  }
  .fleet {
    position: absolute; left: 0; top: 878px; width: 100%; height: 80px;
    display: flex;
  }
  .fleet-item {
    flex: 1; display: flex; flex-direction: column; align-items: center;
  }
  .fleet-item + .fleet-item { border-left: 1px solid var(--line); }
  .fleet:nth-child(n) .fleet-item:nth-child(1) { flex: 0 0 278px; }
  .fleet-item:nth-child(2) { flex: 0 0 261px; }
  .fleet-icon {
    width: 90px; height: 56px; border-radius: 4px;
    background: var(--navy-soft);
  }
  .fleet-label { margin-top: 18px; font-size: 16.5px; font-weight: 500; letter-spacing: 0.3px; }
  .footer {
    position: absolute; left: 0; bottom: 0; width: 100%; height: 65px; display: flex;
  }
  .footer-url {
    width: 548px; background: var(--white); color: var(--navy);
    display: flex; align-items: center; justify-content: center;
    font-size: 21px; font-weight: 500; letter-spacing: 3px;
  }
  .footer-social {
    flex: 1; background: var(--footer-dark);
    display: flex; align-items: center; padding-left: 44px; gap: 14px;
  }
  .social-dot {
    width: 27px; height: 27px; border-radius: 50%;
    border: 1.5px solid var(--white);
  }
</style>
</head>
<body>
  <main class="page">
    <header class="brand">
      <div class="brand-name">VELMORIA</div>
      <div class="brand-tagline">YACHT CHARTER BROKER</div>
    </header>

    <div class="photo photo-deck" role="img" aria-label="Superyacht aft deck with loungers glowing at sunset over calm sea"></div>
    <div class="photo photo-guests" role="img" aria-label="Friends relaxing with drinks on a yacht deck at sunset"></div>
    <div class="photo photo-aerial" role="img" aria-label="Aerial view of a sailing yacht anchored in turquoise water with a snorkeler nearby"></div>

    <section class="motto-panel">
      <div class="motto-frame">
        <div class="motto-line">INHALE,</div>
        <div class="motto-line">EXHALE,</div>
        <div class="motto-strong">SAIL</div>
      </div>
    </section>

    <h2 class="leaders">WE ARE THE LEADERS IN YACHT CHARTERING</h2>

    <section class="fleet">
      <div class="fleet-item">
        <div class="fleet-icon" role="img" aria-label="Line drawing of a monohull sailboat"></div>
        <div class="fleet-label">MONOHULL</div>
      </div>
      <div class="fleet-item">
        <div class="fleet-icon" role="img" aria-label="Line drawing of a catamaran"></div>
        <div class="fleet-label">CATAMARAN</div>
      </div>
      <div class="fleet-item">
        <div class="fleet-icon" role="img" aria-label="Line drawing of a luxury motor yacht"></div>
        <div class="fleet-label">LUXE YACHT</div>
      </div>
    </section>

    <footer class="footer">
      <div class="footer-url">www.velmoriacharters.example</div>
      <div class="footer-social" aria-label="Social media">
        <span class="social-dot"></span>
        <span class="social-dot"></span>
        <span class="social-dot"></span>
        <span class="social-dot"></span>
      </div>
    </footer>
  </main>
</body>
</html>
```